Tarvel Plumbing Solutions

This is for my new plumbing company, I have attached an example of what I’m going for but want it to look better.

Target Market(s)

Home owners, real estate, etc.

Industry/Entity Type

Plumbing

Font styles to use
Other font styles liked:
• As per my logo and other examples uploaded

Colors

Designer to choose colors to be used in the design.

Requirements
Must have
• Must include my logo provided and similar to my flyer I have attached but better

```html
<!DOCTYPE html>
<html lang="en">
<head>
<meta charset="utf-8">
<title>Tarvel Plumbing Solutions – Flyer</title>
<link rel="stylesheet" href="https://fonts.googleapis.com/css2?family=Montserrat:wght@400;500;600;700;800&display=swap">
<style>
  :root {
    --navy: #1c3461;
    --navy-mid: #3a5f92;
    --wave-light: #6f93c0;
    --sky: #94bfe2;
    --sky-pale: #e6edf6;
    --orange: #f36f21;
    --white: #ffffff;
    --ink: #1b2a44;
    --backdrop: #9fc5e6;
  }
  * { box-sizing: border-box; margin: 0; padding: 0; }
  html, body { width: 1200px; height: 1200px; overflow: hidden; }
  body {
    background: var(--backdrop);
    font-family: "Montserrat", sans-serif;
    color: var(--ink);
    position: relative;
  }
  .flyer {
    position: absolute; left: 254px; top: 56px;
    width: 692px; height: 1086px;
    background: var(--white);
    overflow: hidden;
  }
  .brand-header {
    position: absolute; left: 0; top: 0; width: 100%; height: 156px;
    text-align: center;
  }
  .brand-name {
    position: absolute; left: 0; right: 0; top: 44px;
    font-size: 46px; font-weight: 800; letter-spacing: 1px; color: var(--navy);
    line-height: 1;
  }
  .brand-tagline {
    position: absolute; left: 0; right: 0; top: 100px;
    font-size: 15px; font-weight: 600; letter-spacing: 0.5px; color: var(--navy);
  }
  .hero {
    position: absolute; left: 0; top: 156px; width: 100%; height: 321px;
    background: var(--navy);
  }
  .hero-accent-line {
    position: absolute; left: 168px; top: 0; width: 354px; height: 5px;
    background: var(--sky); z-index: 2;
  }
  .hero-wave {
    position: absolute; right: 0; top: 0; width: 360px; height: 100%;
    background: linear-gradient(100deg, rgba(28,52,97,0) 0%, rgba(58,95,146,0.85) 45%, var(--wave-light) 70%, var(--navy-mid) 100%);
  }
  .hero-title {
    position: absolute; left: 44px; top: 50px; width: 520px;
    font-size: 45px; font-weight: 600; line-height: 1.2; color: var(--white);
  }
  .hero-sub {
    position: absolute; left: 44px; top: 186px;
    font-size: 24px; font-weight: 400; line-height: 1.2; color: var(--white);
  }
  .hero-sub strong { font-weight: 600; }
  .discount-badge {
    position: absolute; left: 529px; top: 161px; width: 112px; height: 112px;
    border-radius: 50%; background: var(--orange); color: var(--white);
    display: flex; flex-direction: column; align-items: center; justify-content: center;
    font-size: 17px; font-weight: 500; line-height: 1.25; text-align: center;
  }
  .hero-rule {
    position: absolute; left: 44px; top: 473px; width: 607px; height: 4px;
    background: var(--orange);
  }
  .services-band {
    position: absolute; left: 0; top: 477px; width: 100%; height: 170px;
    background: var(--sky);
  }
  .services-heading {
    position: absolute; left: 44px; top: 495px;
    font-size: 27px; font-weight: 600; color: var(--navy);
  }
  .services-sub {
    position: absolute; left: 44px; top: 530px;
    font-size: 18px; font-weight: 500; color: var(--navy);
  }
  .service-card {
    position: absolute; width: 190px;
    background: var(--sky-pale);
    display: flex; flex-direction: column; align-items: center;
    text-align: center; font-size: 18px; font-weight: 600; line-height: 1.2; color: var(--ink);
  }
  .service-card svg { width: 44px; height: 44px; margin-bottom: 14px; }
  .row-1 { top: 569px; height: 178px; padding-top: 48px; }
  .row-2 { top: 758px; height: 166px; padding-top: 40px; }
  .col-1 { left: 44px; } .col-2 { left: 248px; } .col-3 { left: 456px; }
  .contact-heading {
    position: absolute; left: 44px; top: 957px;
    font-size: 23px; font-weight: 500; color: var(--navy);
  }
  .contact-phone {
    position: absolute; left: 44px; top: 1005px; display: flex; gap: 10px;
    font-size: 15px; line-height: 1.2; color: var(--ink);
  }
  .contact-phone b { font-weight: 700; }
  .contact-mail {
    position: absolute; left: 210px; top: 1016px; display: flex; align-items: center; gap: 8px;
    font-size: 13px; color: var(--ink);
  }
  .social-dots { display: flex; gap: 6px; margin-left: 4px; }
  .social-dot { width: 20px; height: 20px; border-radius: 50%; background: var(--navy); display: inline-block; }
  .cta-button {
    position: absolute; left: 520px; top: 1013px; width: 131px; height: 30px;
    border-radius: 15px; background: var(--orange); color: var(--white);
    font-size: 12px; font-weight: 600; display: flex; align-items: center; justify-content: center;
  }
  .icon { fill: none; stroke: var(--navy); stroke-width: 2; stroke-linecap: round; stroke-linejoin: round; }
</style>
</head>
<body>
  <main class="flyer">
    <header class="brand-header">
      <div class="brand-name">TARVEL</div>
      <div class="brand-tagline">PLUMBING SOLUTIONS</div>
    </header>

    <section class="hero">
      <div class="hero-accent-line"></div>
      <div class="hero-wave" role="img" aria-label="Flowing blue water wave backdrop"></div>
      <h1 class="hero-title">Your Local Reliable Sydney Plumber</h1>
      <p class="hero-sub">Specialising in<br><strong>Plumbing, Drainage &amp;<br>Gas Maintenance.</strong></p>
      <div class="discount-badge"><span>DISCOUNT</span><span>10% OFF</span></div>
    </section>
    <div class="hero-rule"></div>

    <div class="services-band"></div>
    <h2 class="services-heading">OUR SERVICES</h2>
    <p class="services-sub">Reliable Plumbing. Real Solutions</p>

    <div class="service-card row-1 col-1">
      <svg class="icon" viewBox="0 0 44 44"><path d="M8 30 L26 12 L34 20 L16 38 Z"/><path d="M26 12 L32 6 L40 14 L34 20"/><path d="M14 26 C12 30 12 32 14 34 C16 32 16 30 14 26"/></svg>
      Leak Repairs
    </div>
    <div class="service-card row-1 col-2">
      <svg class="icon" viewBox="0 0 44 44"><circle cx="30" cy="12" r="6"/><path d="M26 16 L10 32"/><circle cx="14" cy="30" r="5"/><path d="M20 22 L30 32"/></svg>
      Blocked<br>Drains
    </div>
    <div class="service-card row-1 col-3">
      <svg class="icon" viewBox="0 0 44 44"><path d="M8 40 V12 H26 V22"/><path d="M8 22 H22"/><path d="M30 26 C27 31 27 34 30 36 C33 34 33 31 30 26"/><path d="M32 8 C30 11 30 13 32 14 C34 13 34 11 32 8"/></svg>
      Hot Water
    </div>
    <div class="service-card row-2 col-1">
      <svg class="icon" viewBox="0 0 44 44"><path d="M8 36 L34 10"/><path d="M30 6 L38 14"/><path d="M10 10 L34 34"/><rect x="24" y="26" width="10" height="6" transform="rotate(45 29 29)"/></svg>
      Emergency<br>Plumbing
    </div>
    <div class="service-card row-2 col-2">
      <svg class="icon" viewBox="0 0 44 44"><path d="M10 8 C6 18 14 34 28 36 L32 30 L26 24 L22 28 C18 26 16 22 16 18 L20 14 L14 8 Z"/><path d="M28 10 C32 12 34 14 36 18"/><path d="M28 4 C34 6 38 10 40 16"/></svg>
      Gas Fitting
    </div>
    <div class="service-card row-2 col-3">
      <svg class="icon" viewBox="0 0 44 44"><rect x="18" y="6" width="20" height="26"/><path d="M22 12 H34 M22 18 H34"/><rect x="6" y="20" width="18" height="18"/><path d="M15 25 V33 M11 29 L15 33 L19 29"/></svg>
      Maintenance
    </div>

    <h3 class="contact-heading">CONTACT &amp; SERVICES</h3>
    <div class="contact-phone">
      <svg width="26" height="26" viewBox="0 0 24 24"><path fill="#1b2a44" d="M6.6 10.8a15 15 0 0 0 6.6 6.6l2.2-2.2a1 1 0 0 1 1-.25 11.4 11.4 0 0 0 3.6.57 1 1 0 0 1 1 1V20a1 1 0 0 1-1 1A17 17 0 0 1 3 4a1 1 0 0 1 1-1h3.5a1 1 0 0 1 1 1c0 1.25.2 2.45.57 3.6a1 1 0 0 1-.25 1z"/></svg>
      <div><b>0400 000 000</b><br>Trusted &amp;<br>Local Plumber</div>
    </div>
    <div class="contact-mail">
      <svg width="18" height="14" viewBox="0 0 18 14"><rect x="1" y="1" width="16" height="12" fill="none" stroke="#1b2a44" stroke-width="1.6"/><path d="M1 1 L9 8 L17 1" fill="none" stroke="#1b2a44" stroke-width="1.6"/></svg>
      <span>info@tarvel.com.au</span>
      <span class="social-dots"><span class="social-dot"></span><span class="social-dot"></span><span class="social-dot"></span></span>
    </div>
    <div class="cta-button">CALL US TODAY</div>
  </main>
</body>
</html>
```